Redesign Colorful Business Card

Please redesign the card attached. It is too busy. Please don't eliminate any of the words. The repetivite word "free" can be used less often.

Target Market(s)

College Students.

Contact Information for Business Card

The details listed in the attached image

Font styles to use
Sans Serif

Requirements
Must have
• A clear and simple presentation and must be attractive.

```html
<!DOCTYPE html>
<html lang="en">
<head>
<meta charset="utf-8">
<title>StudyKite Business Card</title>
<link rel="stylesheet" href="https://fonts.googleapis.com/css2?family=Arimo:wght@400;700&display=swap">
<style>
  :root {
    --backdrop: #d4cdcd;
    --card-red: #b30000;
    --panel-green: #064030;
    --bubble-yellow: #fcd21c;
    --star-gold: #f6c21c;
    --text-white: #ffffff;
    --mascot-tone-light: #9a3d6a;
    --mascot-tone-deep: #7c4f63;
  }
  * { margin: 0; padding: 0; box-sizing: border-box; }
  html, body {
    width: 1200px;
    height: 875px;
    overflow: hidden;
    background: var(--backdrop);
    font-family: "Arimo", Arial, sans-serif;
  }
  .card {
    position: absolute;
    left: 230px;
    top: 217px;
    width: 737px;
    height: 439px;
    background: var(--card-red);
    overflow: hidden;
  }
  .brand-name {
    position: absolute;
    left: 44px;
    top: 62px;
    font-size: 26px;
    font-weight: 400;
    color: var(--text-white);
    letter-spacing: 0.2px;
  }
  .mascot-art {
    position: absolute;
    left: 0;
    top: 116px;
    width: 306px;
    height: 323px;
    border-radius: 120px 140px 0 60px;
    background: linear-gradient(135deg, var(--mascot-tone-light), var(--mascot-tone-deep));
  }
  .benefits-panel {
    position: absolute;
    left: 326px;
    top: 124px;
    width: 388px;
    height: 264px;
    background: var(--panel-green);
    border-radius: 30px;
  }
  .free-bubble {
    position: absolute;
    left: 455px;
    top: 79px;
    width: 140px;
    height: 92px;
  }
  .free-bubble-label {
    position: absolute;
    left: 455px;
    top: 96px;
    width: 140px;
    text-align: center;
    font-size: 31px;
    font-weight: 700;
    color: var(--card-red);
  }
  .benefit-list {
    position: absolute;
    left: 315px;
    top: 182px;
    list-style: none;
  }
  .benefit {
    position: relative;
    padding-left: 37px;
    font-size: 21.5px;
    font-weight: 700;
    line-height: 27px;
    color: var(--text-white);
    letter-spacing: 0.2px;
  }
  .benefit + .benefit { margin-top: 14px; }
  .benefit:last-child { margin-top: 19px; }
  .benefit-star {
    position: absolute;
    left: 0;
    top: -1px;
    width: 28px;
    height: 27px;
  }
  .copyright {
    position: absolute;
    left: 249px;
    top: 404px;
    font-size: 15.2px;
    color: var(--text-white);
  }
</style>
</head>
<body>
  <main class="card">
    <p class="brand-name">StudyKite.com</p>

    <div class="mascot-art" role="img" aria-label="Illustration of a trumpeting elephant filled with bright vertical colour stripes"></div>

    <div class="benefits-panel"></div>

    <svg class="free-bubble" viewBox="0 0 140 92" aria-hidden="true">
      <ellipse cx="70" cy="36" rx="69" ry="35" fill="var(--bubble-yellow)"/>
      <path d="M52 64 L42 90 L72 68 Z" fill="var(--bubble-yellow)"/>
    </svg>
    <p class="free-bubble-label">FREE</p>

    <ul class="benefit-list">
      <li class="benefit">
        <svg class="benefit-star" viewBox="0 0 24 24" aria-hidden="true"><path d="M12 1.5l3.1 6.9 7.4.7-5.6 5 1.7 7.4L12 17.6l-6.6 3.9 1.7-7.4-5.6-5 7.4-.7z" fill="var(--star-gold)"/></svg>
        CUT STUDY TIME DOWN BY<br>UP TO 50%
      </li>
      <li class="benefit">
        <svg class="benefit-star" viewBox="0 0 24 24" aria-hidden="true"><path d="M12 1.5l3.1 6.9 7.4.7-5.6 5 1.7 7.4L12 17.6l-6.6 3.9 1.7-7.4-5.6-5 7.4-.7z" fill="var(--star-gold)"/></svg>
        LEARN A SUBJECT WITHOUT<br>HAVING TO GO TO CLASS
      </li>
      <li class="benefit">
        <svg class="benefit-star" viewBox="0 0 24 24" aria-hidden="true"><path d="M12 1.5l3.1 6.9 7.4.7-5.6 5 1.7 7.4L12 17.6l-6.6 3.9 1.7-7.4-5.6-5 7.4-.7z" fill="var(--star-gold)"/></svg>
        MEMORIZE ANYTHING QUICKLY
      </li>
    </ul>

    <p class="copyright">Copyright Kite Study Services, LLC 2013-2022 All Rights Reserved</p>
  </main>
</body>
</html>
```